need label redone so i can edit it, it was ai generated.

Hey, this label design was originally generated by AI, and while I like the overall layout, there are several issues with it. Some elements are not lossless, others appear distorted, uneditable, or low quality.
What I need is a complete recreation of this label—exactly as it is—without adding any new creative touches. Please rebuild every element of the label from scratch, but make sure the final file is in a fully editable, high-resolution format (preferably an .ai file or equivalent).
Each part of the label (text, shapes, background, colors, etc.) should be separated into layers or components so I can easily change anything I want later—like the font, colors, text, or images.
Quality and editability are the top priorities here. Please make sure the design is 100% lossless and flexible for editing.

```html
<!DOCTYPE html>
<html lang="en">
<head>
<meta charset="utf-8">
<title>Tidehound Beach Towel Label</title>
<link rel="stylesheet" href="https://fonts.googleapis.com/css2?family=Figtree:wght@900&family=Barlow+Semi+Condensed:wght@800&family=Oswald:wght@500;600&family=Kalam:wght@700&display=swap">
<style>
  :root {
    --page-bg: #ececec;
    --aqua: #86dde2;
    --aqua-deep: #7ad2d9;
    --navy: #0b4a6e;
    --orange: #e8860f;
    --cream: #efe6cf;
    --yellow: #f7d21a;
    --sand: #f2dcaa;
    --sand-deep: #ecd29c;
    --white: #ffffff;
  }
  * { box-sizing: border-box; margin: 0; padding: 0; }
  html, body {
    width: 1200px; height: 743px; overflow: hidden;
    background: var(--page-bg);
  }
  .label {
    position: absolute; left: 330px; top: 11px;
    width: 540px; height: 720px;
    background: var(--aqua);
    overflow: hidden;
    box-shadow: 0 2px 6px rgba(0,0,0,.15);
  }
  .label-shapes { position: absolute; inset: 0; }
  .brand {
    position: absolute; top: 34px; left: 0; width: 540px;
    display: flex; justify-content: center; align-items: center; gap: 10px;
  }
  .brand-dot { width: 30px; height: 30px; border-radius: 50%; background: var(--navy); }
  .brand-name {
    font-family: "Figtree", sans-serif; font-weight: 900;
    font-size: 46px; letter-spacing: 1px; color: var(--navy); line-height: 1;
  }
  .hero-photo {
    position: absolute; left: 120px; top: 365px; width: 370px; height: 297px;
    border-radius: 0 0 40px 40px;
    background: linear-gradient(180deg, #8fd7ee 0%, #47d3d1 38%, #2fc7c4 50%, #e8eae4 70%, #f3ede0 100%);
  }
  .tagline-pill {
    position: absolute; left: 66px; top: 126px; width: 176px; height: 72px;
    background: var(--orange); border-radius: 40px;
    transform: rotate(-5deg);
    display: flex; flex-direction: column; justify-content: center; align-items: center;
    font-family: "Oswald", sans-serif; font-weight: 600; color: var(--cream);
    line-height: 1.05; text-transform: uppercase;
  }
  .tagline-pill .line-1 { font-size: 23px; }
  .tagline-pill .line-2 { font-size: 18px; }
  .headline {
    position: absolute; left: 72px; top: 228px;
    transform: rotate(-6.5deg); transform-origin: left top;
    font-family: "Barlow Semi Condensed", sans-serif; font-weight: 800;
    color: var(--cream); text-transform: uppercase;
    line-height: 0.95; white-space: nowrap;
  }
  .headline .line-1 { font-size: 64px; display: block; }
  .headline .line-2 { font-size: 67px; display: block; padding-left: 20px; }
  .subline {
    position: absolute; left: 88px; top: 352px;
    transform: rotate(-6.5deg); transform-origin: left top;
    font-family: "Kalam", cursive; font-weight: 700;
    font-size: 21px; color: var(--yellow); white-space: nowrap;
  }
  .badge {
    position: absolute; border-radius: 50%;
    display: flex; flex-direction: column; justify-content: center; align-items: center;
    font-family: "Oswald", sans-serif; font-weight: 600; text-transform: uppercase;
    color: var(--cream); text-align: center; line-height: 1.02;
  }
  .badge-absorbent { left: 52px; top: 408px; width: 100px; height: 100px; background: var(--orange); }
  .badge-absorbent .big { font-family: "Figtree", sans-serif; font-weight: 900; font-size: 40px; line-height: 0.95; text-transform: none; }
  .badge-absorbent .small { font-size: 15px; }
  .badge-bag { left: 146px; top: 479px; width: 102px; height: 102px; background: var(--navy); }
  .badge-bag .big { font-size: 20px; }
  .badge-bag .small { font-size: 11px; margin-top: 2px; }
  .badge-car { left: 51px; top: 526px; width: 100px; height: 100px; background: var(--navy); font-size: 18px; }
  .closing-line {
    position: absolute; left: 45px; top: 663px;
    font-family: "Oswald", sans-serif; font-weight: 600;
    font-size: 19px; line-height: 1.12; color: var(--navy); text-transform: uppercase;
  }
  .feature-icons {
    position: absolute; left: 405px; top: 661px;
    display: flex; gap: 4px; list-style: none;
  }
  .feature {
    width: 27px; display: flex; flex-direction: column; align-items: center;
    font-family: "Oswald", sans-serif; font-weight: 500;
    font-size: 4.6px; line-height: 1.1; color: var(--navy); text-align: center; text-transform: uppercase;
  }
  .feature svg { width: 24px; height: 24px; margin-bottom: 2px; }
</style>
</head>
<body>
<main class="label">
  <svg class="label-shapes" viewBox="0 0 540 720" aria-hidden="true">
    <path class="bg-wave" d="M0 110 C120 90 240 130 360 105 C440 90 500 100 540 95 L540 720 L0 720 Z" fill="var(--aqua-deep)" opacity=".45"/>
    <path class="sand-field" d="M0 507 C60 503 110 500 160 505 L160 720 L0 720 Z" fill="var(--sand)"/>
    <path class="sand-field-right" d="M470 505 C500 495 520 488 540 482 L540 720 L470 720 Z" fill="var(--sand)"/>
    <path class="sand-band" d="M0 630 C120 622 240 640 360 632 C440 626 500 628 540 624 L540 720 L0 720 Z" fill="var(--sand-deep)"/>
  </svg>

  <div class="hero-photo" role="img" aria-label="Photo of a smiling golden retriever sitting on a tropical beach wrapped in a turquoise microfiber towel"></div>

  <svg class="label-shapes" viewBox="0 0 540 720" aria-hidden="true">
    <path class="headline-banner" d="M44 230 C44 205 58 195 92 191 C190 178 290 150 380 138 C450 128 494 142 497 190 L490 378 C400 384 250 390 130 398 C75 402 48 388 46 355 Z" fill="var(--navy)"/>
  </svg>

  <header class="brand">
    <span class="brand-dot"></span>
    <span class="brand-name">TIDEHOUND</span>
  </header>

  <div class="tagline-pill">
    <span class="line-1">Dry your dog</span>
    <span class="line-2">faster than ever!</span>
  </div>

  <h1 class="headline">
    <span class="line-1">Dry your dog</span>
    <span class="line-2">in seconds</span>
  </h1>
  <p class="subline">The Ultimate Beach Towel For Dogs</p>

  <div class="badge badge-absorbent">
    <span class="big">5x</span>
    <span class="small">More</span>
    <span class="small">Absorbent</span>
  </div>
  <div class="badge badge-bag">
    <span class="big">Beach</span>
    <span class="big">Bag</span>
    <span class="small">Must-have</span>
  </div>
  <div class="badge badge-car">
    <span>No more</span>
    <span>wet car</span>
    <span>rides</span>
  </div>

  <p class="closing-line">Trade the stack of<br>towels for one that works</p>

  <ul class="feature-icons">
    <li class="feature">
      <svg viewBox="0 0 24 24"><circle cx="12" cy="12" r="11" fill="var(--white)" stroke="var(--navy)" stroke-width="1.2"/><rect x="7.5" y="6.5" width="9" height="11" rx="1.5" fill="none" stroke="var(--navy)" stroke-width="1.2"/><circle cx="12" cy="13" r="2.6" fill="none" stroke="var(--navy)" stroke-width="1.2"/></svg>
      Machine<br>washable
    </li>
    <li class="feature">
      <svg viewBox="0 0 24 24"><circle cx="12" cy="12" r="11" fill="var(--white)" stroke="var(--navy)" stroke-width="1.2"/><path d="M12 5 C9 9 8 11 8 13.5 A4 4 0 0 0 16 13.5 C16 11 15 9 12 5 Z" fill="var(--navy)"/></svg>
      Fast<br>drying
    </li>
    <li class="feature">
      <svg viewBox="0 0 24 24"><circle cx="12" cy="12" r="11" fill="var(--white)" stroke="var(--navy)" stroke-width="1.2"/><path d="M7 13 A5 5 0 0 1 15 8 M17 11 A5 5 0 0 1 9 16" fill="none" stroke="var(--navy)" stroke-width="1.4"/><path d="M15 6 L15.5 8.5 L13 9 M9 18 L8.5 15.5 L11 15" fill="none" stroke="var(--navy)" stroke-width="1.2"/></svg>
      Eco<br>friendly
    </li>
  </ul>
</main>
</body>
</html>
```